lunch promotion flyer

we recently started a new menu, would like to distribute the new menu and offer to the local office worker and residents.

Promotion Offer:
Pick any 2 delicious western Yum Cha for only $12
( Offer valid until 28/2/2015)
Updates

The flyer should contain the full menu and highlight the promotion, not just the promotion offer, it is totally wrong.

Target Market(s)

local office workers and local residents,

office workers are mainly working for the banks

Industry/Entity Type

Office

```html
<!DOCTYPE html>
<html lang="en">
<head>
<meta charset="utf-8">
<title>Western Yum Cha – Lunch Menu</title>
<link href="https://fonts.googleapis.com/css2?family=Archivo:wght@700;800&family=Rye&family=Pathway+Gothic+One&family=Dosis:wght@500&display=swap" rel="stylesheet">
<style>
:root{
  --wood-dark:#3a2014;
  --wood-mid:#6b4128;
  --wood-light:#8a5a38;
  --red:#9b0d0d;
  --red-dark:#6e0606;
  --paper:#ecd6a4;
  --paper-edge:#d7b77a;
  --ink:#2a1a0e;
  --white:#ffffff;
}
*{margin:0;padding:0;box-sizing:border-box}
html,body{width:849px;height:1200px;overflow:hidden;background:var(--wood-dark)}
.flyer{position:relative;width:849px;height:1200px;overflow:hidden;
  background:
    repeating-linear-gradient(180deg,transparent 0 112px,rgba(20,8,2,.55) 112px 115px),
    linear-gradient(180deg,#5a3521 0%,#7a4c2e 25%,#5c3722 50%,#7b4d2f 75%,#4d2c1a 100%);}
.top-band{position:absolute;left:0;top:0;width:849px;height:10px;background:var(--red)}
.headline{position:absolute;left:0;top:38px;width:849px;text-align:center;
  font-family:"Archivo",Arial,sans-serif;font-weight:800;color:var(--white);
  font-size:50px;line-height:58px;text-shadow:3px 3px 4px rgba(0,0,0,.6)}
.headline .big{font-size:58px}
.art{position:absolute;left:0;top:0}
.new-menu{position:absolute;left:20px;top:538px;font-family:"Rye",serif;font-size:31px;color:var(--white);
  letter-spacing:1px;text-shadow:2px 2px 3px rgba(0,0,0,.5)}
.new-menu::before,.new-menu::after{content:"";position:absolute;left:0;right:0;height:2px;background:var(--white)}
.new-menu::before{top:-2px}.new-menu::after{bottom:-1px}
.paper{position:absolute;left:0;top:585px}
.menu{position:absolute;top:627px;font-family:"Pathway Gothic One",sans-serif;color:var(--ink)}
.menu h2{font-weight:400;font-size:13px;margin-bottom:2px}
.menu-left{left:25px;width:360px}
.menu-right{right:26px;width:440px;text-align:right}
.item{display:grid;grid-template-columns:1fr 36px 22px;font-size:10px;line-height:15.7px;white-space:nowrap}
.item .tag,.item .price{text-align:center}
.menu-right .item{grid-template-columns:1fr 26px 30px}
.menu-right .item .name{text-align:right;padding-right:6px}
.bagels{margin-top:9px}
.section-gap{margin-top:22px}
.legend{position:absolute;right:26px;top:883px;font-family:"Pathway Gothic One",sans-serif;font-size:12px;color:var(--ink)}
.hours{position:absolute;left:0;top:966px;width:849px;text-align:center;font-family:"Dosis",sans-serif;font-weight:500;
  color:var(--white);font-size:19px;line-height:22px;text-shadow:1px 1px 2px rgba(0,0,0,.6)}
.hours .lead{font-size:19px}
.rule{position:absolute;left:160px;top:1080px;width:560px;height:4px;background:var(--red)}
.contact{position:absolute;top:1106px;width:420px;text-align:center;font-family:"Dosis",sans-serif;font-weight:500;
  color:var(--white);font-size:13px;line-height:14px;text-shadow:1px 1px 2px rgba(0,0,0,.6)}
.contact-left{left:52px}
.contact-right{left:445px}
.bottom-band{position:absolute;left:0;bottom:0;width:849px;height:10px;background:var(--red)}
</style>
</head>
<body>
<main class="flyer">
  <div class="top-band"></div>
  <h1 class="headline">Pick any 2 delicious western<br><span class="big">Yum Cha for only $12</span></h1>

  <svg class="art" width="849" height="560" viewBox="0 0 849 560">
    <defs>
      <linearGradient id="photoTone" x1="0" y1="0" x2="1" y2="1">
        <stop offset="0" stop-color="#5b4638"/>
        <stop offset=".45" stop-color="#c9a36d"/>
        <stop offset="1" stop-color="#3b2c24"/>
      </linearGradient>
      <radialGradient id="circleTone" cx=".5" cy=".5" r=".6">
        <stop offset="0" stop-color="#e6d2ad"/>
        <stop offset="1" stop-color="#b98d58"/>
      </radialGradient>
    </defs>
    <path d="M0 164 Q420 178 849 188 L849 200 Q420 190 0 176 Z" fill="var(--red)"/>
    <path d="M0 178 Q420 192 849 202 L849 535 Q420 510 0 485 Z" fill="url(#photoTone)" role="img" aria-label="Photo of yum cha table with bamboo steamers, dumplings, pastries and tea cups"/>
    <path d="M0 485 Q420 510 849 535 L849 552 Q420 526 0 500 Z" fill="var(--red)"/>
    <circle cx="770" cy="372" r="158" fill="var(--red)"/>
    <circle cx="770" cy="372" r="150" fill="url(#circleTone)" role="img" aria-label="Close-up photo of assorted dumplings in bamboo steamers"/>
  </svg>

  <div class="new-menu">NEW MENU</div>

  <svg class="paper" width="849" height="370" viewBox="0 0 849 370">
    <defs>
      <linearGradient id="paperTone" x1="0" y1="0" x2="1" y2="1">
        <stop offset="0" stop-color="#f0dcaa"/>
        <stop offset=".5" stop-color="#e7cf98"/>
        <stop offset="1" stop-color="#dcbd80"/>
      </linearGradient>
    </defs>
    <path d="M0 8 L40 2 L90 10 L150 0 L220 9 L300 3 L360 12 L430 4 L500 10 L560 1 L630 9 L700 3 L760 11 L810 4 L849 9 L849 345 L800 352 L740 343 L680 355 L610 346 L540 358 L470 347 L400 356 L330 345 L260 357 L190 346 L120 356 L60 347 L0 353 Z" fill="url(#paperTone)" stroke="var(--paper-edge)" stroke-width="2"/>
  </svg>

  <section class="menu menu-left">
    <h2>Western Yum Cha</h2>
    <div class="item"><span class="name">Spanish Serrano ham &amp;cauliflower croquettes w saffron aioli</span><span class="tag"></span><span class="price">9</span></div>
    <div class="item"><span class="name">Spicy beef meatballs w rich tomato sugo&amp; yoghurt</span><span class="tag">GF</span><span class="price">8</span></div>
    <div class="item"><span class="name">Garlic&amp; chili prawns- pan fried w crusty bread</span><span class="tag"></span><span class="price">13</span></div>
    <div class="item"><span class="name">Potato bravas – crispy fried potato wSpanishspicytomato aioli</span><span class="tag">V/GF</span><span class="price">6</span></div>
    <div class="item"><span class="name">Pesto arancini – Italian risotto ball w aioli</span><span class="tag"></span><span class="price">7</span></div>
    <div class="item"><span class="name">Beef shaslicks – marinated porterhouse beef, onion&amp; capsicum</span><span class="tag"></span><span class="price">13</span></div>
    <div class="item"><span class="name">Vegetarian rice paper rolls w hoisin dipping sauce</span><span class="tag">VG/GF</span><span class="price">7</span></div>
    <div class="item"><span class="name">Crispy calamari – lightly fried waioli &amp; lemon</span><span class="tag">GF</span><span class="price">11</span></div>
    <div class="item"><span class="name">Bruschetta –warmed tomatoes , Spanish onion, basil &amp; fetta w balsamic glaze</span><span class="tag">V</span><span class="price">9</span></div>
    <div class="item"><span class="name">Chicken drumettes, oven roasted w spicy plum sauce&amp; sesame seeds</span><span class="tag"></span><span class="price">8</span></div>
    <div class="item"><span class="name">Sweet corn &amp;coriander fritters, crunchy fried fritter w guacamole</span><span class="tag">V</span><span class="price">9</span></div>
    <div class="item"><span class="name">sweet potato wafers , sumac salt seasoning w aioli</span><span class="tag">GF</span><span class="price">7</span></div>
    <div class="item"><span class="name">Dips w warm Turkish pide</span><span class="tag"></span><span class="price">14</span></div>
    <h2 class="bagels">Bagels</h2>
    <div class="item"><span class="name">Smoked Salmon, dill cream cheese &amp; rocket</span><span class="tag"></span><span class="price">12</span></div>
    <div class="item"><span class="name">Chicken, cranberry &amp; brie</span><span class="tag"></span><span class="price">12</span></div>
    <div class="item"><span class="name">Prosciutto, roast capsicum, semi-dried tomato, rocket</span><span class="tag"></span><span class="price">12</span></div>
  </section>

  <section class="menu menu-right">
    <h2>Salads</h2>
    <div class="item"><span class="name">Cucumber, honey dew w goats cheese dressing (+ chicken)</span><span class="tag">V</span><span class="price">11 (14)</span></div>
    <div class="item"><span class="name">Rice noodlesw crispy calamari &amp; vegetables</span><span class="tag">GF</span><span class="price">13</span></div>
    <div class="item"><span class="name">Thai beefwAsian vegetables, lemongrass and crushed nuts</span><span class="tag"></span><span class="price">13</span></div>
    <div class="item"><span class="name">Gourmet tomatomedley&amp;mixed beansw basil dressing</span><span class="tag">VG</span><span class="price">10</span></div>
    <div class="item"><span class="name">Smoked salmonw tomato, Spanish onion &amp; fetta</span><span class="tag">GF</span><span class="price">12</span></div>
    <h2 class="section-gap">Something substantial &amp; classic</h2>
    <div class="item"><span class="name">Porterhouse steak sandwich with rocket, roast peppers, onions, cheese, dijonaise with chips</span><span class="tag"></span><span class="price">17.5</span></div>
    <div class="item"><span class="name">Classic Fish &amp; Chips, lightly fried fish with garden salad &amp; Chips</span><span class="tag"></span><span class="price">17.5</span></div>
    <div class="item"><span class="name">Chicken Parma -</span><span class="tag"></span><span class="price"></span></div>
    <div class="item"><span class="name">house-made crumbed breast, Napoli sauce, ham, topped with mozzarella cheese with chips &amp; salad</span><span class="tag"></span><span class="price">17.5</span></div>
  </section>

  <p class="legend">GF = Gluten Free&nbsp; V = Vegetarian VG = Vegan</p>

  <div class="hours">
    <p class="lead">We welcome you on:</p>
    <p>Monday – Wednesday 11.30 am – 4 pm</p>
    <p>Thursday 11.30 am – 7 pm</p>
    <p>Friday – Saturday 11.30 am – late</p>
  </div>

  <div class="rule"></div>

  <div class="contact contact-left">
    <p>Catering, Private &amp; Corporate functions available</p>
    <p>(7 am – 1 am)</p>
    <p>Enquiries: 03 9000 4821</p>
    <p>function@quaysidekitchen.example</p>
    <p>www.quaysidekitchen.example</p>
  </div>
  <div class="contact contact-right">
    <p>Join us at:</p>
    <p>Waterfront side, Ground Floor, Meridian building</p>
    <p>Shop 2, 150 Pier Lane, Docklands</p>
    <p>03 9000 4821</p>
    <p>catering@quaysidekitchen.example</p>
  </div>
  <div class="bottom-band"></div>
</main>
</body>
</html>
```